MOLVIKAN Hemp based Pet Brand that growns it's own premium hemp and creates amazing pet products.

We need packaging designed for a new company based in South West Florida. We grow our own hemp with our other company Fern 9 Vat and use the harvest to make our hemp based pet products. Our initial products are pet treats that include Soft Chews and Calming Chews. The bags come in two different sizes. Regular bag being 7x10.25 inches and Small bag 4.25X6.25 inches. We also need a tincture box and label created. We want packaging that will catch the eye of the consumer and colors that compliment our logo. Dropper label size is 4x1.75 inches and the milligram of CBD is 1500. We have attached our manufacturers packaging and would like you to coppy everything other than their overall design and logo. Use default UPC and QR code, which we can replace later in the Ai file. Please see all the attached documents and please ask me if you have any questions. The final design should communicate a premium product that stand our from the rest. Something that catches the eye of the consumer by its premium appearance. Packaging is everything so I hope you can use your creative skills to create something special!

Target Market(s)

Pet owners

Font styles to use
Serif
Sans Serif

Colors
0054AA
0677BA
7BADD7
CADEEF
E8F1F8
0094D4
00A9DD
6FCCEA
C7EBF8
E9F6FB
EE7325
F08F49
F5BC92
FAE3D3
FDF4ED

Requirements
Must have
• Stand out design. Premium feel. Imagine shopping for something for your pet and seeing a brand that POPS and just looks like a good product because the packaging is so good.
Nice to have
• Modern mature feel
Should not have
• Cartoony feeling. Do not use baby blue everywhere. Do not include pictures of people in the packaging

```html
<!DOCTYPE html>
<html lang="en">
<head>
<meta charset="UTF-8">
<title>MOLVIKAN Calming Chews – Bag Front</title>
<link rel="stylesheet" href="https://fonts.googleapis.com/css2?family=Montserrat:wght@700;800;900&display=swap">
<style>
  :root {
    --brand-deep: #0054AA;
    --brand-mid: #0677BA;
    --brand-bright: #0094D4;
    --brand-accent: #00A9DD;
    --white: #FFFFFF;
    --photo-dark: #4A2E1C;
    --photo-mid: #8A5A35;
    --photo-light: #D9CFC4;
  }
  html, body {
    margin: 0;
    padding: 0;
    overflow: hidden;
    background: var(--white);
  }
  .package {
    position: relative;
    width: 1200px;
    height: 2700px;
    overflow: hidden;
    background: linear-gradient(160deg, var(--brand-bright) 0%, var(--brand-mid) 60%, var(--brand-deep) 100%);
    font-family: "Montserrat", Arial, sans-serif;
  }
  .brand-name {
    position: absolute;
    left: 70px;
    top: 110px;
    display: flex;
    align-items: center;
    gap: 22px;
    color: var(--white);
    font-weight: 800;
    font-size: 64px;
    letter-spacing: 8px;
  }
  .brand-name .brand-dot {
    width: 34px;
    height: 34px;
    border-radius: 50%;
    background: var(--white);
  }
  .hero-photo {
    position: absolute;
    left: 150px;
    top: 530px;
    width: 1050px;
    height: 1520px;
    border-radius: 420px 420px 0 0;
    background:
      radial-gradient(ellipse at 50% 30%, var(--photo-mid) 0%, var(--photo-dark) 55%, transparent 75%),
      linear-gradient(180deg, var(--photo-mid) 0%, var(--photo-dark) 45%, var(--photo-light) 80%);
  }
  .white-panel {
    position: absolute;
    left: 0;
    top: 0;
    width: 1200px;
    height: 2700px;
  }
  .product-title {
    position: absolute;
    left: 22px;
    top: 2015px;
    margin: 0;
    line-height: 0.82;
    font-weight: 900;
  }
  .product-title .title-main {
    display: block;
    font-size: 230px;
    letter-spacing: -7px;
    color: var(--brand-accent);
  }
  .product-title .title-sub {
    display: block;
    font-size: 150px;
    letter-spacing: -4px;
    color: var(--brand-mid);
    margin-left: 18px;
  }
  .tagline-pill {
    position: absolute;
    left: 64px;
    top: 2323px;
    width: 444px;
    height: 107px;
    border-radius: 0 54px 54px 0;
    background: var(--brand-accent);
    color: var(--white);
    font-weight: 800;
    font-size: 48px;
    letter-spacing: 1px;
    display: flex;
    align-items: center;
    padding-left: 18px;
    box-sizing: border-box;
  }
  .ingredients {
    position: absolute;
    left: 66px;
    top: 2442px;
    margin: 0;
    font-weight: 700;
    font-size: 50px;
    line-height: 64px;
    letter-spacing: 1px;
    color: var(--brand-mid);
  }
  .quality-mark {
    position: absolute;
    left: 783px;
    top: 2437px;
    display: flex;
    align-items: center;
    gap: 6px;
    color: var(--brand-mid);
    font-weight: 700;
    font-size: 40px;
  }
  .quality-mark svg {
    width: 88px;
    height: 88px;
  }
  .net-content {
    position: absolute;
    left: 0;
    width: 1200px;
    top: 2638px;
    text-align: center;
    color: var(--brand-mid);
    font-weight: 800;
    font-size: 26px;
    letter-spacing: 1px;
  }
  .net-content .divider {
    margin: 0 28px;
  }
</style>
</head>
<body>
  <main class="package">
    <div class="brand-name"><span class="brand-dot"></span><span>MOLVIKAN</span></div>

    <div class="hero-photo" role="img" aria-label="Photo of a smiling brown and white Australian Shepherd dog looking forward"></div>

    <svg class="white-panel" viewBox="0 0 1200 2700" aria-hidden="true">
      <rect x="-300" y="1135" width="720" height="1700" rx="290" fill="#FFFFFF"/>
      <rect x="610" y="1250" width="900" height="1600" rx="300" fill="#FFFFFF"/>
      <path d="M0 2700 L0 1900 L420 1900 L420 1950 A95 95 0 0 0 610 1950 L610 1900 L1200 1900 L1200 2700 Z" fill="#FFFFFF"/>
    </svg>

    <h1 class="product-title">
      <span class="title-main">CALMING</span>
      <span class="title-sub">CHEWS</span>
    </h1>

    <div class="tagline-pill">RELAX &amp; CALM</div>

    <p class="ingredients">With Organic Hemp<br>&amp; CBDa</p>

    <div class="quality-mark">
      <svg viewBox="0 0 88 88" aria-hidden="true">
        <circle cx="42" cy="46" r="36" fill="none" stroke="#00A9DD" stroke-width="6"/>
        <path d="M24 46 L38 60 L78 14" fill="none" stroke="#00A9DD" stroke-width="10" stroke-linecap="round" stroke-linejoin="round"/>
      </svg>
      <span>Farm grown</span>
    </div>

    <div class="net-content">NET CT. 10<span class="divider">|</span>NET WT. 2oz</div>
  </main>
</body>
</html>
```